Home page design for dealership

Client is a truck dealership out of Dallas that wants a rustic/vintage design-themed website. Prefers to have vintage design details over the use of cowboy or western images, and so, is open to the use of different color schemes.
The focus of the website must be the inventory, with a large centerpiece image about 950 x 400 pixels. The centerpiece becomes a rotating slideshow, in the next stage of ‘buildout’, with a coded website.
Need 3 ‘button’ graphics that will link and include a hover effect.

Dealership info:
Halvorsen Autos
28417 Brinmoor Lane
Pellham, TX 75940
972-418-3926

We need a website design that follows this layout:
-Background - wood panels
-Accent Colors - open to any scheme
-Banner - 950 pixels wide – includes dealer name and phone number with KL, Chirpo and Vexa+ icons
-Navigation/Menu Bar – tabs – Home | Inventory | Finance | Vehicle Finder | About Us | Contact Us
-Centerpiece image – 950 x 400 pixels – any newer model truck
-Call-to-action buttons – use your judgment for placement, show the hover effect on one ‘button’
View Our Inventory
Find your Dream Truck
Finance your Truck
-Content section - will include a column for dealer address and hours, and a second column for ‘Welcome to Halvorsen Autos’ copy(attached). Also needs to accommodate the following logos: Vinlog, QTC A+, Zupo
Hours: Mon-Fri: 9a – 6p, Sat-Sun: 12p – 6p
-Featured Inventory – row of thumbnails that preview client’s inventory

Below are a few example sites of what client likes:
http://www.orchardgin-example.com/ - likes the clean look of the wood background
http://lumbrimarkatt-example.net/ - likes the simple look of paper against wood
https://plumvalefair-example.com/ - Likes the burnt edges effect on the paper background

This dealership sells pickup trucks. For example: Brant K270, Corvan Q48, Tokara Ridgeback. For the centerpiece image, please use a newer model from the examples provided.

```html
<!DOCTYPE html>
<html lang="en">
<head>
<meta charset="utf-8">
<title>Halvorsen Autos — Home</title>
<link rel="stylesheet" href="https://fonts.googleapis.com/css2?family=Lato:wght@400;700&family=Figtree:wght@600;700&family=Michroma&display=swap">
<style>
:root{
  --wood-dark:#2b1a14;
  --wood-mid:#5c4a3b;
  --wood-top:#3a2a20;
  --paper:#ffffff;
  --paper-tan:#d0c3b3;
  --paper-light:#ebe7e0;
  --ink:#4a3b30;
  --ink-soft:#5a4a3c;
  --green:#8a9a1a;
  --orange:#f07d1f;
  --blue:#3b8fd8;
  --rule:#d6d2cc;
}
*{margin:0;padding:0;box-sizing:border-box}
html,body{width:1200px;height:1000px;overflow:hidden;background:var(--paper)}
body{position:relative;font-family:"Lato",sans-serif;color:var(--ink)}
.top-band{position:absolute;left:0;top:0;width:1200px;height:100px;background:linear-gradient(var(--wood-dark),var(--wood-mid))}
.tagline{position:absolute;top:2px;width:100%;text-align:center;color:#f2ece4;font-size:21px;font-family:"Lato",sans-serif}
.cta{position:absolute;top:61px;width:300px;height:160px;background:#22150f;overflow:hidden}
.cta .photo{position:absolute;right:0;top:0;width:190px;height:160px;clip-path:polygon(8% 0,100% 0,100% 100%,0 100%,6% 70%,2% 45%,10% 20%)}
.cta .label{position:absolute;left:17px;top:38px;font-family:"Michroma",sans-serif;font-size:19px;line-height:27px;color:#fff;font-weight:700}
.cta .label b{font-weight:700}
.cta-inventory{left:120px}.cta-inventory b{color:var(--green)}
.cta-find{left:450px}.cta-find b{color:var(--orange)}
.cta-finance{left:780px}.cta-finance b{color:var(--blue)}
.welcome{position:absolute;left:119px;top:247px;width:632px;font-size:16px;line-height:25.5px;color:var(--ink)}
.welcome p{margin-bottom:26px}
.welcome hr{border:0;border-top:2px solid var(--rule);margin:4px 0 24px}
.welcome a{color:var(--green);font-weight:700;text-decoration:none}
.dealer-card{position:absolute;left:780px;top:251px;width:300px;height:290px;background:var(--paper-light);padding:16px 19px;font-size:16px;line-height:25.5px}
.dealer-card h2{font-size:16px;font-weight:700;text-transform:uppercase}
.dealer-card hr{border:0;border-top:2px solid var(--rule);margin:17px 0 12px}
.dealer-card .map{position:absolute;left:20px;top:209px;width:60px;height:60px;border:2px solid var(--green);background:linear-gradient(135deg,#e8e4dc,#c9c4b8)}
.dealer-card .directions{position:absolute;left:90px;top:210px;width:200px}
.dealer-card a{color:var(--green);font-weight:700;text-decoration:none}
.torn{position:absolute;left:0;top:578px}
.featured{position:absolute;left:0;top:630px;width:1200px;height:220px;background:var(--paper-tan)}
.featured h2{position:absolute;top:-8px;width:100%;text-align:center;font-family:"Figtree",sans-serif;font-weight:700;font-size:23px;color:var(--ink-soft)}
.arrow{position:absolute;top:40px;width:20px;height:115px;background:var(--green)}
.arrow svg{position:absolute;left:6px;top:50px}
.thumb{position:absolute;top:40px;width:160px;height:115px}
.featured .more{position:absolute;top:174px;width:100%;text-align:center;font-family:"Figtree",sans-serif;font-weight:700;font-size:16px;color:var(--ink-soft)}
.featured .more a{color:var(--green);text-decoration:none}
.hours-band{position:absolute;left:0;top:850px;width:1200px;height:70px;background:var(--wood-mid);color:#fff}
.hours{position:absolute;left:118px;top:12px;font-size:16px;line-height:23px}
.hours h3{font-size:16px;font-weight:700}
.partners{position:absolute;right:118px;top:18px;display:flex;align-items:center;gap:26px;color:#c9bfb3;font-size:26px}
.partner-badge{display:flex;align-items:center;gap:10px}
.partner-badge .seal{width:92px;height:34px;background:#c9bfb3;border-radius:3px}
.partner-badge .dot{width:24px;height:24px;border-radius:50%;background:#c9bfb3}
.footer{position:absolute;left:0;top:920px;width:1200px;height:80px;background:var(--wood-dark)}
.copyright{position:absolute;left:118px;top:14px;font-size:12px;color:#9c8a78;font-weight:700}
.nav{position:absolute;right:121px;top:13px;display:flex;gap:24px;list-style:none}
.nav a{font-family:"Figtree",sans-serif;font-weight:700;font-size:13px;color:var(--green);text-decoration:none;text-transform:uppercase}
</style>
</head>
<body>
<header class="top-band">
  <p class="tagline">reputation for selling high quality used cars backed by extraordinary service ...</p>
</header>

<a class="cta cta-inventory" href="#inventory">
  <div class="photo" role="img" aria-label="Black pickup truck front view" style="background:linear-gradient(135deg,#cfcbc4,#3a3a3c 55%,#1b1b1d)"></div>
  <div class="label"><b>VIEW</b><br>Our<br>Inventory</div>
</a>
<a class="cta cta-find" href="#finder">
  <div class="photo" role="img" aria-label="Orange off-road pickup truck in the desert" style="background:linear-gradient(160deg,#b9a48c,#d0612a 50%,#6b4a33)"></div>
  <div class="label"><b>FIND</b> your<br>Dream<br>Truck</div>
</a>
<a class="cta cta-finance" href="#finance">
  <div class="photo" role="img" aria-label="Blue pickup truck in a green field" style="background:linear-gradient(170deg,#c8d8e6,#2b4fa0 50%,#5a7a3a)"></div>
  <div class="label"><b>FINANCE</b><br>your<br>Truck</div>
</a>

<main class="welcome">
  <p>Most of our business is done with individuals who’ve never even driven the vehicle or seen it in person prior to purchasing. Only two things make that possible: unequaled quality and a high level of service.</p>
  <p>We offer a variety of car financing programs to meet the individual needs of our customers, and provide our customers with a variety of extended warranty plans to protect their used car after a purchase has been made.</p>
  <hr>
  <p><a href="#inventory">Click here to browse our current inventory</a> and learn more about us. If you have any questions please feel free to call us at <strong>214-418-3926.</strong></p>
</main>

<aside class="dealer-card">
  <h2>Halvorsen Autos</h2>
  <div>28417 Brinmoor Lane</div>
  <div>Pellham, TX 75940</div>
  <hr>
  <div><strong>Telephone</strong> 972-418-3926</div>
  <hr>
  <h2>How to find us</h2>
  <div class="map" role="img" aria-label="Small map of the showroom location"></div>
  <div class="directions"><a href="#map">Click here</a> to find directions to our showroom</div>
</aside>

<svg class="torn" width="1200" height="54" viewBox="0 0 1200 54" aria-hidden="true">
  <path fill="#d0c3b3" d="M285 54 L300 40 L312 30 L330 26 L350 22 L380 20 L400 14 L430 16 L460 12 L490 14 L520 8 L545 10 L560 4 L590 10 L620 8 L650 12 L680 6 L700 10 L730 8 L760 4 L780 12 L800 10 L820 16 L840 22 L855 34 L870 54 Z"/>
</svg>

<section class="featured">
  <h2>Some of our current vehicles</h2>
  <div class="arrow" style="left:120px"><svg width="8" height="14"><path d="M7 0 L0 7 L7 14Z" fill="#d6dea0"/></svg></div>
  <div class="thumb" style="left:160px;background:linear-gradient(#c9ccc8,#2a2a30 60%,#8a8a86)" role="img" aria-label="Black Corvan Q48 pickup"></div>
  <div class="thumb" style="left:340px;background:linear-gradient(#d8d4c8,#3a3632 55%,#6c8a3a)" role="img" aria-label="Dark grey Corvan Q48 pickup on grass"></div>
  <div class="thumb" style="left:520px;background:linear-gradient(#b9c0c4,#4a4a46 55%,#8a7a68)" role="img" aria-label="Grey Tokara Ridgeback pickup"></div>
  <div class="thumb" style="left:700px;background:linear-gradient(#c4ccd4,#2a4aa8 55%,#8a8a86)" role="img" aria-label="Blue Tokara Ridgeback pickup"></div>
  <div class="thumb" style="left:880px;background:linear-gradient(#b8c8da,#1e2430 55%,#8a8e90)" role="img" aria-label="Black Brant K270 pickup"></div>
  <div class="arrow" style="left:1060px"><svg width="8" height="14"><path d="M0 0 L7 7 L0 14Z" fill="#d6dea0"/></svg></div>
  <p class="more">We have a large number of cars available today! <a href="#inventory">- View our full inventory ›</a></p>
</section>

<section class="hours-band">
  <div class="hours">
    <h3>Our Opening Times</h3>
    <div>Mon-Fri: 9a – 6p, Sat-Sun: 12p – 6p</div>
  </div>
  <div class="partners">
    <span>Zupo</span>
    <span class="partner-badge" role="img" aria-label="QTC A+ accreditation"><span class="seal"></span><span class="dot"></span></span>
    <span>Vinlog</span>
  </div>
</section>

<footer class="footer">
  <p class="copyright">© Copyright 2014 Halvorsen Autos . All rights reserved</p>
  <ul class="nav">
    <li><a href="#home">Home</a></li>
    <li><a href="#inventory">Inventory</a></li>
    <li><a href="#finance">Finance</a></li>
    <li><a href="#finder">Vehicle Finder</a></li>
    <li><a href="#about">About</a></li>
    <li><a href="#contact">Contact</a></li>
  </ul>
</footer>
</body>
</html>
```